Vacation Rental business needs a prospective client flyer

We are a short-term vacation rental company in Steamboat Springs, Colorado called "Brisk Pine Lodges". We are looking to find new clients in the area by handing out flyers to the local Realtors to recommend using us to their clients.

We would like to touch on our low management fee of 18% and are local hands on approach.

Logo sheet is included for color and logo use.

```html
<!DOCTYPE html>
<html lang="en">
<head>
<meta charset="utf-8">
<title>Brisk Pine Lodges – Flyer</title>
<link href="https://fonts.googleapis.com/css2?family=Open+Sans:ital,wght@0,300;0,400;0,600;0,700;1,600&display=swap" rel="stylesheet">
<style>
  :root {
    --blue: #12709f;
    --blue-dark: #0d5c85;
    --gray: #4e4d4d;
    --gray-light: #8a8a8a;
    --white: #ffffff;
    --stage: #3a3a3a;
    --ink: #3f3f3f;
  }
  * { margin: 0; padding: 0; box-sizing: border-box; }
  html, body { width: 800px; height: 1200px; overflow: hidden; background: var(--stage); }
  body { position: relative; font-family: "Open Sans", Arial, sans-serif; }

  .flyer {
    position: absolute; left: 0; top: 33px;
    width: 822px; height: 1165px;
    transform: scale(0.9732); transform-origin: top left;
    background: var(--white); overflow: hidden;
  }
  .flyer-shapes { position: absolute; inset: 0; }

  .brand { position: absolute; left: 29px; top: 30px; color: var(--blue); }
  .brand-name { font-size: 40px; font-weight: 400; letter-spacing: -0.5px; line-height: 1; }
  .brand-place { margin-top: 16px; font-size: 17px; letter-spacing: 5.4px; color: #5c5c5c; font-weight: 400; }

  .welcome {
    position: absolute; left: 60px; width: 702px; top: 220px;
    text-align: center; color: var(--white); font-size: 22px; line-height: 29px; font-weight: 400;
  }

  .section-pill {
    position: absolute; left: 386px; top: 331px; width: 315px; height: 71px;
    display: flex; align-items: center; justify-content: center;
    color: var(--white); font-size: 30px; font-weight: 600;
  }

  .services { position: absolute; top: 419px; list-style: none; }
  .services li {
    display: flex; align-items: center; gap: 9px; height: 29px;
    color: var(--blue); font-size: 16.5px; font-style: italic; font-weight: 600;
  }
  .services svg { width: 21px; height: 18px; fill: var(--blue); flex: none; }
  .services-left { left: 278px; }
  .services-right { left: 524px; }

  .fee-badge {
    position: absolute; left: 115px; top: 442px; width: 124px; height: 124px; border-radius: 50%;
    background: var(--blue); color: var(--white); text-align: center;
    box-shadow: 0 0 0 6px var(--white);
  }
  .fee-badge .arrow { display: block; margin: 14px auto 0; width: 0; height: 0;
    border-left: 12px solid transparent; border-right: 12px solid transparent; border-top: 20px solid var(--white); }
  .fee-value { font-size: 40px; font-weight: 700; line-height: 40px; margin-top: 2px; }
  .fee-label { font-size: 13px; line-height: 15px; font-weight: 600; }

  .offer-box {
    position: absolute; left: 501px; top: 541px; width: 278px; height: 94px;
    border: 1.5px solid var(--gray-light); border-radius: 22px; background: var(--white);
    text-align: center; color: var(--ink); font-size: 14px; line-height: 17px; padding-top: 12px;
  }
  .offer-cta {
    position: absolute; left: 28px; top: 70px; width: 222px; height: 32px; border-radius: 16px;
    background: var(--gray); color: var(--white); font-size: 14px; line-height: 32px;
  }

  .about-title { position: absolute; left: 27px; top: 598px; color: var(--white); font-size: 28px; font-weight: 400; }
  .about-rule { position: absolute; left: 27px; top: 640px; width: 294px; height: 1px; background: var(--white); }
  .about-rule-bold { position: absolute; left: 321px; top: 638px; width: 98px; height: 5px; background: var(--white); }
  .about-copy { position: absolute; left: 28px; top: 657px; width: 345px; color: var(--white); font-size: 15.5px; line-height: 19px; }
  .about-copy p + p { margin-top: 19px; }

  .gallery-item { position: absolute; width: 94px; height: 94px; border-radius: 50%;
    border: 3px solid var(--white); box-shadow: 0 0 0 2px #6b6b6b inset; }

  .website { position: absolute; left: 455px; top: 982px; display: flex; align-items: center; gap: 18px;
    color: var(--white); font-size: 25px; font-weight: 600; }
  .website svg { width: 36px; height: 36px; }

  .brand-footer { position: absolute; left: 0; width: 412px; top: 1008px; text-align: center; color: var(--blue); }
  .brand-footer .brand-name { font-size: 26px; }
  .brand-footer .brand-place { margin-top: 7px; font-size: 11px; letter-spacing: 3.6px; }
  .footer-rule { position: absolute; left: 29px; top: 1073px; width: 393px; height: 1px; background: var(--blue); }

  .accreditation { position: absolute; left: 38px; top: 1095px; width: 117px; height: 43px; border-radius: 5px; background: var(--blue); }

  .contact { position: absolute; top: 1099px; display: flex; align-items: center; gap: 12px;
    color: var(--blue); font-size: 23px; font-weight: 400; }
  .contact svg { fill: var(--blue); }
  .contact-phone { left: 202px; }
  .contact-email { left: 440px; gap: 16px; }
</style>
</head>
<body>
<main class="flyer">
  <svg class="flyer-shapes" viewBox="0 0 822 1165" width="822" height="1165" aria-hidden="false">
    <defs>
      <linearGradient id="cabin" x1="0" y1="0" x2="1" y2="1">
        <stop offset="0" stop-color="#8a6a55"/>
        <stop offset="0.5" stop-color="#6e4b3a"/>
        <stop offset="1" stop-color="#3e2a22"/>
      </linearGradient>
    </defs>
    <rect class="hero-photo" x="0" y="0" width="822" height="520" fill="url(#cabin)" role="img" aria-label="Photo of a couple relaxing on a sofa in a cosy log cabin, with a snowy window behind them"/>
    <path class="hero-mask" d="M0 0 H441 C420 80 320 115 210 140 C110 165 45 215 0 282 Z" fill="var(--white)"/>
    <line x1="251" y1="294" x2="561" y2="294" stroke="var(--white)" stroke-width="1"/>
    <path class="band-blue" d="M0 430 C100 380 250 360 390 358 L700 355 C760 340 800 280 822 220 V720 H0 Z" fill="var(--blue)"/>
    <path class="band-white" d="M0 518 C80 452 220 405 390 402 L700 402 C760 390 800 330 822 285 V720 H0 Z" fill="var(--white)"/>
    <rect x="386" y="331" width="315" height="71" rx="30" fill="var(--blue)"/>
    <path class="about-gray" d="M0 535 C150 520 300 560 450 620 C560 665 640 700 700 690 C760 680 800 650 822 625 V1000 L450 900 H0 Z" fill="var(--gray)"/>
    <path class="about-blue" d="M0 575 C140 548 280 572 420 640 C520 690 560 700 600 760 C680 880 760 980 822 1015 V1022 C720 1070 620 1075 500 1045 C380 1012 220 985 100 1010 C60 1020 20 1035 0 1046 Z" fill="var(--blue)"/>
  </svg>

  <div class="brand">
    <div class="brand-name">Brisk Pine Lodges</div>
    <div class="brand-place">steamboat springs, co</div>
  </div>

  <p class="welcome">Welcome to Brisk Pine Lodges! Our properties in Steamboat Springs have everything you need for a great vacation!</p>

  <h2 class="section-pill">Guest Services</h2>

  <ul class="services services-left">
    <li><svg viewBox="0 0 21 18"><rect x="2" y="5" width="14" height="7" rx="2"/><circle cx="5" cy="15" r="2"/><circle cx="14" cy="15" r="2"/><rect x="15" y="2" width="5" height="2"/></svg>Baby Equipment Rentals</li>
    <li><svg viewBox="0 0 21 18"><path d="M1 3 H20 V7 A2 2 0 0 0 20 11 V15 H1 V11 A2 2 0 0 0 1 7 Z"/></svg>Discounted Lift Tickets</li>
    <li><svg viewBox="0 0 21 18"><path d="M2 2 H19 L20 7 H1 Z"/><rect x="3" y="8" width="15" height="8"/></svg>Grocery Delivery</li>
    <li><svg viewBox="0 0 21 18"><circle cx="10.5" cy="9" r="6"/><rect x="1" y="2" width="2" height="14"/><rect x="18" y="2" width="2" height="14"/></svg>Local Dining</li>
  </ul>
  <ul class="services services-right">
    <li><svg viewBox="0 0 21 18"><path d="M10.5 1 L20 9 H17 V17 H4 V9 H1 Z"/></svg>Property Management Services</li>
    <li><svg viewBox="0 0 21 18"><circle cx="12" cy="3" r="2"/><path d="M6 7 L13 6 L12 12 L17 15 L16 16 L9 12 Z"/><rect x="1" y="15" width="19" height="1.5" transform="rotate(-12 10 16)"/></svg>Discounted Ski and Bike Rentals</li>
    <li><svg viewBox="0 0 21 18"><path d="M1 10 L20 6 L20 8 L12 11 L8 17 L6 17 L8 12 L3 13 L1 11 Z"/></svg>Travel Insurance</li>
  </ul>

  <div class="fee-badge">
    <span class="arrow"></span>
    <div class="fee-value">18%</div>
    <div class="fee-label">management<br>fee</div>
  </div>

  <div class="offer-box">
    We offer a wide range of<br>properties that all include WiFi,<br>Full Kitchens, Hot Tubs and more.
    <div class="offer-cta">Book directly with us today!</div>
  </div>

  <h2 class="about-title">ABOUT US</h2>
  <div class="about-rule"></div>
  <div class="about-rule-bold"></div>
  <div class="about-copy">
    <p>We have 36 years of combined experience in vacation rentals, investment properties, residential real estate and construction.</p>
    <p>We believed that there had to be a better vacation rental company so we started it! We are hands-on from the beginning to the end of every reservation. We treat every property as if it were our own and every guest as if they were our family. We love what we do and love Steamboat!</p>
    <p>We are locally operated and locally owned right here in Steamboat Springs, Colorado. No corporate offices, no franchises – Just a local couple who works hard and gets it done!</p>
  </div>

  <div class="gallery-item" style="left:389px;top:747px;background:linear-gradient(#7fb2e0,#4f8a4a)" role="img" aria-label="Photo of a lodge exterior with pine trees"></div>
  <div class="gallery-item" style="left:494px;top:747px;background:linear-gradient(#4a5f84,#6a4a35)" role="img" aria-label="Photo of a living room interior"></div>
  <div class="gallery-item" style="left:594px;top:747px;background:linear-gradient(#8ab6e2,#c9b493)" role="img" aria-label="Photo of a townhouse exterior"></div>
  <div class="gallery-item" style="left:694px;top:747px;background:linear-gradient(#6f9fd2,#c97a5a)" role="img" aria-label="Photo of a condo building in snow"></div>
  <div class="gallery-item" style="left:389px;top:852px;background:linear-gradient(#9cc3e8,#7c8f5c)" role="img" aria-label="Photo of a resort building on a hillside"></div>
  <div class="gallery-item" style="left:494px;top:852px;background:linear-gradient(#e3ddd2,#8c6e55)" role="img" aria-label="Photo of a bright apartment interior"></div>
  <div class="gallery-item" style="left:594px;top:852px;background:linear-gradient(#a89a86,#5e4a3c)" role="img" aria-label="Photo of a dining area with mountain view"></div>
  <div class="gallery-item" style="left:694px;top:852px;background:linear-gradient(#5f9a4c,#86c4e0)" role="img" aria-label="Photo of an outdoor pool surrounded by trees"></div>

  <div class="website">
    <svg viewBox="0 0 36 36"><circle cx="18" cy="18" r="17" fill="var(--white)"/><path d="M8 10 C12 8 16 10 15 14 C14 17 10 16 10 20 C10 24 7 22 5 18 C4 14 6 11 8 10 Z M20 6 C25 7 30 11 31 16 C28 16 26 19 27 23 C27 27 22 30 20 28 C18 24 22 21 19 18 C17 15 21 12 20 6 Z" fill="var(--blue)"/></svg>
    <span>briskpinelodges.com</span>
  </div>

  <div class="brand-footer">
    <div class="brand-name">Brisk Pine Lodges</div>
    <div class="brand-place">steamboat springs, co</div>
  </div>
  <div class="footer-rule"></div>

  <div class="accreditation" role="img" aria-label="Accreditation badge"></div>

  <div class="contact contact-phone">
    <svg viewBox="0 0 24 24" width="26" height="26"><path d="M6.6 2 L10 6.5 L7.8 9.2 C9 11.8 12 14.8 14.8 16.2 L17.5 14 L22 17.4 L19.6 21.4 C11 21 3 13 2.6 4.4 Z"/></svg>
    <span>(970) 555-0148</span>
  </div>
  <div class="contact contact-email">
    <svg viewBox="0 0 36 26" width="36" height="26"><path d="M1 1 H35 V25 H1 Z M4 3 L18 15 L32 3" fill="none" stroke="var(--blue)" stroke-width="2.5"/></svg>
    <span>info@briskpinelodges.com</span>
  </div>
</main>
</body>
</html>
```